" A Empresa se chama Vento Sul Hotéis. Somos uma empresa do ramo hoteleiro. Esta é a marca da Holding que participa em todos os empreendimentos que administramos. Somos novos no mercado hoteleiro mas temos mais de 30 anos de tradiçao no mercado de construçao e imóveis. "

```html
<!DOCTYPE html>
<html lang="pt-BR">
<head>
<meta charset="utf-8">
<title>Vento Sul Hotéis — Envelope Carta</title>
<link href="https://fonts.googleapis.com/css2?family=Montserrat:wght@400;500&display=swap" rel="stylesheet">
<style>
  :root {
    --bg: #e9e7e4;
    --paper: #ffffff;
    --orange: #ef7d32;
    --ink: #6b6b6b;
  }
  html, body {
    margin: 0;
    padding: 0;
    width: 1200px;
    height: 1200px;
    overflow: hidden;
    background: var(--bg);
  }
  .envelope-dieline {
    display: block;
    width: 1200px;
    height: 1200px;
  }
  .brand-name {
    font-family: "Montserrat", sans-serif;
    font-weight: 500;
    fill: var(--orange);
  }
  .contact-line {
    font-family: "Montserrat", sans-serif;
    font-weight: 400;
    fill: var(--ink);
  }
</style>
</head>
<body>
<svg class="envelope-dieline" viewBox="0 0 500 500" xmlns="http://www.w3.org/2000/svg">
  <!-- body with side flaps and bottom flap -->
  <path class="envelope-body" fill="var(--paper)"
        d="M78 111 L50 138 L50 296 L86 301 L66 432 Q65 442 75 442 L432 442 Q442 442 441 432 L417 301 L455 296 L455 138 L428 111 Z"/>
  <!-- top closing flap -->
  <path class="envelope-top-flap" fill="var(--orange)"
        d="M78 111 L96 70 Q100 62 110 62 L398 62 Q408 62 411 70 L428 111 Z"/>

  <!-- front branding -->
  <text class="brand-name" x="100" y="164" font-size="13">Vento Sul Hotéis</text>

  <!-- fold guides -->
  <line x1="78" y1="323" x2="108" y2="323" stroke="var(--orange)" stroke-width="1.6"/>
  <line x1="394" y1="323" x2="428" y2="323" stroke="var(--orange)" stroke-width="1.6"/>

  <!-- back flap branding, printed upside down -->
  <g class="flap-branding" transform="rotate(180 255 341)">
    <text class="contact-line" x="255" y="330" font-size="4" text-anchor="middle">Rua das Gaivotas 210, Loja 04 - Niterói - RJ</text>
    <text class="contact-line" x="255" y="337" font-size="4" text-anchor="middle">www.ventosulhoteis.com.br</text>
    <text class="brand-name" x="255" y="355" font-size="11" text-anchor="middle">Vento Sul Hotéis</text>
  </g>
</svg>
</body>
</html>
```